Your 'not so average' farmers. We are farmers and entrepreneurs trying to connect the great divide.

KTB (Brosmere Holdings Inc) is a family owned farm (in our 3rd generation). We grow vegetables (corn, soy, potatoes, snap beans) but we also invest in and grow businesses. These other businesses can be non-farming related businesses. We are family oriented, environmentally concise, and active in our small community. We need a business card to hand out to our fellow farmers, businesses we would like to partner with and invest in, and community members. So, we need a card with a natural, 'tenders of the land' feel for the farmers but no overly so that we seem centered on farming for the other businesses. We would like it to have our Company info (name, number, email, phone, fax) then Personal info for us five who run the joint (Name, phone, email). So we will order 100 cards for each 5 who work at KTB (500total) that is professional, not boring or hokey, but catching and unique.
Target Market(s)
Farmers, Business Owners, Investors, Community Members
Industry/Entity Type
Farming
Contact Information for Business Card
Office info on one side:
Brosmere Holdings Inc.
1187 Larkin Rd.
Pell Hollow, WI 54872
Office: (608) 555-0417
Fax: (608) 555-0283
brosmereoffice@quillpost.example
Personal Info for the 5 who run KTB. Everybody will have their own personal info on their cards(maybe on the other side):
Name
Mobile
Email
Look and feel

```html
<!DOCTYPE html>
<html lang="en">
<head>
<meta charset="utf-8">
<title>Brosmere Holdings Inc. – Business Cards</title>
<link rel="stylesheet" href="https://fonts.googleapis.com/css2?family=Cabin:wght@600;700&family=PT+Sans+Narrow:wght@400;700&display=swap">
<style>
  :root {
    --brand-red: #a51d1d;
    --brand-green: #0b7340;
    --deep-brown: #4a170c;
    --label-brown: #7d4c3f;
    --ink: #2a211c;
    --muted-ink: #4f4a46;
    --band-text: #d9d6d2;
    --card-center: #efeee6;
    --card-edge: #c8c7c7;
    --illustration: #6b4a40;
    --page: #ffffff;
  }
  * { margin: 0; padding: 0; box-sizing: border-box; }
  html, body { width: 1200px; height: 715px; overflow: hidden; background: var(--page); }
  body { position: relative; font-family: "PT Sans Narrow", "Arial Narrow", sans-serif; }

  .card {
    position: absolute;
    width: 578px;
    height: 340px;
    background: radial-gradient(ellipse at 45% 55%, var(--card-center) 0%, #e2e1db 45%, var(--card-edge) 100%);
    overflow: hidden;
  }
  .card--office { left: 314px; top: 13px; }
  .card--personal-red { left: 13px; top: 371px; --accent: var(--brand-red); }
  .card--personal-green { left: 616px; top: 371px; --accent: var(--brand-green); }

  /* Office side */
  .company-name {
    position: absolute; left: 0; width: 459px; top: 20px;
    text-align: center;
    font-family: "Cabin", sans-serif; font-weight: 700;
    font-variant: small-caps; font-size: 36px; letter-spacing: 0.5px;
    color: var(--deep-brown);
  }
  .swoosh { position: absolute; left: 70px; top: 62px; }
  .farm-illustration {
    position: absolute; left: 28px; top: 80px; width: 413px; height: 120px;
    background: radial-gradient(ellipse at center, #7a574c 0%, #6b4a40 55%, rgba(107,74,64,0.15) 100%);
    opacity: 0.85;
    border-radius: 4px;
  }
  .divider-line {
    position: absolute; left: 459px; top: 0; width: 5px; height: 340px;
    background: var(--deep-brown);
  }
  .tagline-band {
    position: absolute; left: 469px; top: 0; width: 109px; height: 340px;
    background: var(--brand-red);
    border-radius: 5px 0 0 5px;
  }
  .tagline {
    position: absolute; left: 469px; top: 30px; width: 109px; height: 290px;
    writing-mode: vertical-rl;
    display: flex; align-items: center;
    font-size: 31px; color: var(--band-text); letter-spacing: 0.5px;
  }
  .side-tab {
    position: absolute; left: 0; width: 34px; height: 74px;
    background: var(--accent, var(--brand-red));
    border-radius: 0 5px 5px 0;
  }
  .card--office .side-tab { top: 222px; }
  .address, .office-contacts {
    position: absolute; top: 222px;
    font-weight: 700; font-size: 21px; line-height: 26px;
    color: var(--deep-brown);
  }
  .address { left: 47px; }
  .office-contacts { right: 137px; text-align: right; }
  .office-contacts .label { color: var(--label-brown); }

  /* Personal side */
  .personal-band { position: absolute; left: 452px; top: 0; }
  .person-name {
    position: absolute; left: 0; width: 482px; top: 70px;
    text-align: center;
    font-family: "Cabin", sans-serif; font-weight: 700; font-size: 40px;
    color: var(--accent);
  }
  .name-swoosh { position: absolute; left: 161px; top: 113px; }
  .person-contacts {
    position: absolute; left: 0; width: 482px; top: 134px;
    text-align: center; font-weight: 700; font-size: 22px; line-height: 29px;
    color: var(--ink);
  }
  .card--personal-red .person-contacts .label { color: var(--muted-ink); }
  .card--personal .side-tab { top: 130px; }
  .band-company {
    position: absolute; left: 469px; top: 26px; width: 109px; height: 290px;
    writing-mode: vertical-rl;
    display: flex; align-items: center;
    font-weight: 700; font-size: 23px; letter-spacing: 2px;
    color: var(--band-text);
  }
</style>
</head>
<body>

  <section class="card card--office">
    <h1 class="company-name">Brosmere Holdings Inc.</h1>
    <svg class="swoosh" width="320" height="8" viewBox="0 0 320 8" aria-hidden="true">
      <path d="M0 4 Q160 0 320 4 Q160 8 0 4Z" fill="var(--deep-brown)"/>
    </svg>
    <div class="farm-illustration" role="img" aria-label="Illustration of a windmill between two picket fences"></div>
    <div class="divider-line"></div>
    <div class="tagline-band"></div>
    <p class="tagline">SOME TAGLINE HERE</p>
    <div class="side-tab"></div>
    <address class="address" style="font-style:normal">1187 Larkin Rd.<br>Pell Hollow,<br>WI 54872.</address>
    <p class="office-contacts">
      <span class="label">Office :</span>(608) 555-0417<br>
      <span class="label">Fax :</span>(608) 555-0283<br>
      brosmereoffice@quillpost.example
    </p>
  </section>

  <section class="card card--personal card--personal-red">
    <div class="side-tab"></div>
    <svg class="personal-band" width="126" height="340" viewBox="0 0 126 340" aria-hidden="true">
      <path d="M22 0 H126 V340 H22 V198 L12 164 L22 130 Z" fill="var(--accent)"/>
    </svg>
    <h2 class="person-name">JOHN DOE</h2>
    <svg class="name-swoosh" width="160" height="6" viewBox="0 0 160 6" aria-hidden="true">
      <path d="M0 3 Q80 0 160 3 Q80 6 0 3Z" fill="var(--accent)"/>
    </svg>
    <p class="person-contacts"><span class="label">Mobile:</span> (608) 555-0417<br>brosmereoffice@quillpost.example</p>
    <p class="band-company">BROSMERE HOLDINGS INC.</p>
  </section>

  <section class="card card--personal card--personal-green">
    <div class="side-tab"></div>
    <svg class="personal-band" width="126" height="340" viewBox="0 0 126 340" aria-hidden="true">
      <path d="M22 0 H126 V340 H22 V198 L12 164 L22 130 Z" fill="var(--accent)"/>
    </svg>
    <h2 class="person-name">JOHN DOE</h2>
    <svg class="name-swoosh" width="160" height="6" viewBox="0 0 160 6" aria-hidden="true">
      <path d="M0 3 Q80 0 160 3 Q80 6 0 3Z" fill="var(--accent)"/>
    </svg>
    <p class="person-contacts"><span class="label">Mobile :</span>(608) 555-0417<br>brosmereoffice@quillpost.example</p>
    <p class="band-company">BROSMERE HOLDINGS INC.</p>
  </section>

</body>
</html>
```